kiPlume Landing Page 2

Edit the attached page to make it more visually appealing and professional. This page is a landing page that will direct our viewers to our rallyvant page. The join buttons definitely need to be changed, as well as fonts for the whole page. Please put rallyvant logo on the "join us" button, and put chatterpod and blipster with logos on the bottom center. If there are any further questions please ask us. http://kiplume.moravist.com/hands.html

Target Market(s)

Middle class Americans ages 20-35.

Industry/Entity Type

It Professional

```html
<!DOCTYPE html>
<html lang="en">
<head>
<meta charset="utf-8">
<title>kiPlume — Join Us</title>
<link rel="stylesheet" href="https://fonts.googleapis.com/css2?family=Francois+One&family=Oswald:wght@400;600&family=Vollkorn:wght@700&display=swap">
<style>
  :root {
    --ink-dark: #0d0d0d;
    --photo-mid: #5a5a5a;
    --photo-light: #b8b8b8;
    --headline-red: #e8172b;
    --tagline-teal: #1d8fb3;
    --white: #ffffff;
    --button-ink: #111111;
    --rallyvant-mark: #d93a7c;
  }
  * { margin: 0; padding: 0; box-sizing: border-box; }
  html, body {
    width: 1200px;
    height: 675px;
    overflow: hidden;
    background: var(--ink-dark);
  }
  .landing {
    position: relative;
    width: 1200px;
    height: 675px;
    overflow: hidden;
  }
  .hero-photo {
    position: absolute;
    inset: 0;
    background:
      radial-gradient(ellipse 48% 62% at 58% 48%, var(--photo-light) 0%, var(--photo-mid) 45%, transparent 78%),
      radial-gradient(ellipse 40% 40% at 15% 55%, #4a4a4a 0%, transparent 70%),
      var(--ink-dark);
  }
  .brand-name {
    position: absolute;
    left: 22px;
    top: 22px;
    font-family: "Oswald", sans-serif;
    font-weight: 600;
    font-size: 44px;
    color: var(--white);
    letter-spacing: 0.5px;
  }
  .message {
    position: absolute;
    left: 0;
    right: 0;
    top: 166px;
    text-align: center;
    margin-left: 60px;
  }
  .headline {
    font-family: "Francois One", sans-serif;
    font-size: 56px;
    line-height: 1;
    color: var(--headline-red);
    text-transform: uppercase;
    letter-spacing: 0.5px;
  }
  .tagline {
    margin-top: 12px;
    font-family: "Vollkorn", serif;
    font-weight: 700;
    font-size: 38px;
    line-height: 50px;
    color: var(--tagline-teal);
    text-shadow: 1px 2px 0 var(--white);
  }
  .join-button {
    position: absolute;
    left: 451px;
    top: 378px;
    width: 355px;
    height: 86px;
    border-radius: 43px;
    background: var(--white);
    display: flex;
    align-items: center;
    gap: 14px;
    padding-left: 22px;
    text-decoration: none;
  }
  .join-button__mark {
    width: 58px;
    height: 58px;
    flex: none;
  }
  .join-button__label {
    font-family: "Oswald", sans-serif;
    font-weight: 400;
    font-size: 58px;
    letter-spacing: 4px;
    word-spacing: 14px;
    color: var(--button-ink);
    line-height: 1;
  }
  .social-links {
    position: absolute;
    left: 0;
    right: 0;
    top: 608px;
    display: flex;
    justify-content: center;
    gap: 48px;
    margin-left: 26px;
  }
  .social-links__name {
    font-family: "Oswald", sans-serif;
    font-weight: 600;
    font-size: 44px;
    color: var(--white);
    text-decoration: none;
    line-height: 1;
  }
</style>
</head>
<body>
  <main class="landing">
    <div class="hero-photo" role="img" aria-label="Black and white close-up photograph of two hands tightly clasped together"></div>

    <div class="brand-name">kiPlume</div>

    <section class="message">
      <h1 class="headline">You are the change you seek.</h1>
      <p class="tagline">protecting your family and your<br>future requires your action.</p>
    </section>

    <a class="join-button" href="http://kiplume.moravist.com/hands.html" aria-label="Join us on rallyvant">
      <svg class="join-button__mark" viewBox="0 0 58 58" aria-hidden="true">
        <circle cx="29" cy="29" r="26" fill="var(--rallyvant-mark)"/>
      </svg>
      <span class="join-button__label">JOIN US</span>
    </a>

    <nav class="social-links">
      <a class="social-links__name" href="#">chatterpod</a>
      <a class="social-links__name" href="#">blipster</a>
    </nav>
  </main>
</body>
</html>
```